Quorvel Properties - Chat n’ Clink Evening Graphic Invite

We need a graphic design for a corporate reception that we are calling Chat n’ Clink Evening. The invite should read:

"QVR invites you to join us at Chat n’ Clink Evening

Monday, Jan 22nd
6:30 - 8:30 pm EST

Tallow Grill - Lounge Room

48213 E Harrow Glen Rd
Solbrook, FL 33417

Join us for excellent wine and tasty bites at our semi-annual PDA reception. Swing by whenever you can – timing is casual and we'd love to see you there!"

Please feel free to use fun photos from the Tallow Grill gallery: https://www.tallowgrillexample.com/photos

Also, please use the QVR logo attached.

Target Market(s)

Corporate professional

Colors
0054AA
0677BA
7BADD7
CADEEF
E8F1F8

Requirements
Must have
• QVR logo, attached verbiage

```html
<!DOCTYPE html>
<html lang="en">
<head>
<meta charset="utf-8">
<title>Chat n’ Clink Evening – Invitation</title>
<link href="https://fonts.googleapis.com/css2?family=Great+Vibes&family=Montserrat:wght@200;400;700&display=swap" rel="stylesheet">
<style>
  :root {
    --navy: #1f3a7d;
    --royal: #0054aa;
    --page: #e9ebee;
    --paper: #ffffff;
    --mist: #e4e7ec;
  }
  * { margin: 0; padding: 0; box-sizing: border-box; }
  html, body { width: 1200px; height: 1200px; overflow: hidden; background: var(--page); }
  .canvas { position: relative; width: 1200px; height: 1200px; }
  .invite {
    position: absolute; left: 190px; top: 34px; width: 820px; height: 1132px;
    background: radial-gradient(ellipse at 70% 30%, var(--mist) 0%, var(--paper) 55%), var(--paper);
    overflow: hidden;
    font-family: "Montserrat", Arial, sans-serif;
    color: var(--navy);
  }
  .gallery { position: absolute; left: 0; top: 0; width: 820px; height: 1132px; }
  .copy { position: absolute; right: 42px; text-align: right; white-space: nowrap; }
  .intro { top: 40px; font-size: 25px; line-height: 44px; font-weight: 400; }
  .title-script { top: 150px; font-family: "Great Vibes", cursive; font-size: 74px; line-height: 80px; }
  .title-main { top: 200px; font-size: 84px; line-height: 100px; font-weight: 200; letter-spacing: -1px; }
  .date { top: 333px; font-size: 25px; line-height: 38px; font-weight: 700; }
  .time { top: 376px; font-size: 23px; line-height: 38px; font-weight: 400; }
  .venue { top: 449px; font-size: 25px; line-height: 38px; font-weight: 700; }
  .address { top: 498px; font-size: 23px; line-height: 39px; font-weight: 400; }
  .message { top: 606px; font-size: 23px; line-height: 39px; font-weight: 400; }
  .brand {
    position: absolute; right: 42px; top: 1000px;
    display: flex; align-items: center; gap: 12px;
    font-size: 40px; font-weight: 700; color: var(--navy); line-height: 1;
  }
  .brand-square { width: 30px; height: 30px; background: var(--navy); }
</style>
</head>
<body>
<div class="canvas">
  <div class="invite">
    <svg class="gallery" viewBox="0 0 1290 1780" preserveAspectRatio="none" xmlns="http://www.w3.org/2000/svg">
      <defs>
        <linearGradient id="woodTone" x1="0" y1="0" x2="1" y2="1">
          <stop offset="0" stop-color="#b06a30"/>
          <stop offset="1" stop-color="#7c4520"/>
        </linearGradient>
        <linearGradient id="roomTone" x1="0" y1="0" x2="0" y2="1">
          <stop offset="0" stop-color="#9ea4ad"/>
          <stop offset="0.45" stop-color="#6e5b48"/>
          <stop offset="1" stop-color="#2e2620"/>
        </linearGradient>
        <radialGradient id="barTone" cx="0.5" cy="0.7" r="0.7">
          <stop offset="0" stop-color="#b5452a"/>
          <stop offset="1" stop-color="#1c1210"/>
        </radialGradient>
      </defs>
      <polygon points="0,0 345,0 685,335 405,612 685,893 410,1170 685,1440 345,1780 0,1780" fill="var(--navy)"/>
      <polygon role="img" aria-label="Overhead photo of plated dishes and wine on a wooden table" points="164,0 340,0 670,335 400,605 250,470 120,600 0,480 0,164" fill="url(#woodTone)"/>
      <polygon role="img" aria-label="Photo of a cocktail being stirred at the bar" points="0,1180 400,1180 675,1440 340,1780 175,1780 0,1605" fill="url(#barTone)"/>
      <polygon role="img" aria-label="Photo of the restaurant lounge room with tables and flowers" points="250,470 670,893 250,1318 0,1068 0,720" fill="url(#roomTone)"/>
      <polyline points="250,470 670,893 250,1318" fill="none" stroke="var(--navy)" stroke-width="9"/>
      <polyline points="345,0 685,335 405,612" fill="none" stroke="var(--navy)" stroke-width="9"/>
      <polyline points="410,1170 685,1440 345,1780" fill="none" stroke="var(--navy)" stroke-width="9"/>
    </svg>

    <p class="copy intro">QVR invites you<br>to join us at</p>
    <p class="copy title-script">Chat n’ Clink</p>
    <p class="copy title-main">Evening</p>
    <p class="copy date">Monday, Jan 22nd</p>
    <p class="copy time">6:30 - 8:30 pm EST</p>
    <p class="copy venue">Tallow Grill - Lounge Room</p>
    <p class="copy address">48213 E Harrow Glen Rd<br>Solbrook, FL 33417</p>
    <p class="copy message">Join us for excellent wine<br>and tasty bites at our<br>semi-annual PDA reception.<br>Swing by whenever<br>you can – timing is casual<br>and we'd love to<br>see you there!</p>

    <div class="brand"><span class="brand-square"></span><span class="brand-name">QVR</span></div>
  </div>
</div>
</body>
</html>
```